Business cards for law firm with global theme

I'd like business cards with contact info for two offices. They should include the colors and font of the new logo design, which is a stylized globe with an "F" in it. The feel should be very modern and professional.

```html
<!DOCTYPE html>
<html lang="en">
<head>
<meta charset="UTF-8">
<title>Valmont Law – Business Cards</title>
<link rel="stylesheet" href="https://fonts.googleapis.com/css2?family=Montserrat:wght@400;500;700;800&display=swap">
<style>
  :root {
    --navy: #173f73;
    --navy-deep: #12325d;
    --sky: #29a8e0;
    --paper: #ffffff;
    --ink: #2d2f36;
    --stage: #2a2a2d;
  }
  * { margin: 0; padding: 0; box-sizing: border-box; }
  html, body {
    width: 1200px; height: 900px; overflow: hidden;
    background: var(--stage);
    font-family: "Montserrat", sans-serif;
  }
  .canvas { position: relative; width: 1200px; height: 900px; }

  .card {
    position: absolute;
    width: 640px; height: 366px;
    border-radius: 16px;
    overflow: hidden;
    box-shadow: 0 10px 28px rgba(0,0,0,.45);
  }

  .brand { position: absolute; display: flex; align-items: center; white-space: nowrap; }
  .brand-dot { border-radius: 50%; flex: none; }
  .brand-name { font-weight: 700; text-transform: uppercase; line-height: 1; white-space: nowrap; }

  /* Back face */
  .card-back { left: 90px; top: 60px; background: var(--navy); }
  .card-back .brand { left: 290px; top: 150px; gap: 14px; }
  .card-back .brand-dot { width: 26px; height: 26px; background: var(--paper); }
  .card-back .brand-name { font-size: 34px; letter-spacing: 1px; color: var(--paper); }

  /* Front face */
  .card-front { left: 470px; top: 480px; background: var(--paper); }
  .card-front .brand { left: 40px; top: 104px; gap: 12px; }
  .card-front .brand-dot { width: 42px; height: 42px; background: var(--sky); }
  .card-front .brand-name { font-size: 26px; letter-spacing: .5px; color: var(--navy); }

  .person { position: absolute; right: 36px; top: 46px; text-align: right; white-space: nowrap; }
  .person-name {
    font-weight: 800; font-size: 22px; letter-spacing: 1px;
    color: var(--navy); text-transform: uppercase;
  }
  .person-name .surname { color: var(--sky); }
  .person-role { font-weight: 400; font-size: 14px; color: var(--ink); margin-top: 2px; }

  .contact {
    position: absolute; left: 44px; top: 170px;
    font-size: 14px; color: var(--ink); line-height: 1.45;
  }
  .offices { display: flex; gap: 28px; margin-bottom: 6px; }
  .contact-line { display: flex; align-items: center; gap: 8px; }
  .contact-line svg { width: 12px; height: 12px; flex: none; }

  .wave { position: absolute; left: 0; bottom: 0; width: 640px; height: 366px; }
</style>
</head>
<body>
<main class="canvas">

  <section class="card card-back" aria-label="Card back">
    <div class="brand">
      <span class="brand-dot"></span>
      <span class="brand-name">Valmont Law</span>
    </div>
  </section>

  <section class="card card-front" aria-label="Card front">
    <svg class="wave" viewBox="0 0 640 366" aria-hidden="true">
      <path d="M0,318 C170,322 330,300 440,236 C520,190 580,170 640,168 L640,366 L0,366 Z" fill="var(--sky)"/>
      <path d="M0,326 C180,328 340,310 450,248 C530,204 585,184 640,182 L640,366 L0,366 Z" fill="var(--paper)"/>
      <path d="M0,332 C185,334 345,318 455,256 C535,212 588,192 640,190 L640,366 L0,366 Z" fill="var(--navy)"/>
    </svg>

    <div class="brand">
      <span class="brand-dot"></span>
      <span class="brand-name">Valmont Law</span>
    </div>

    <div class="person">
      <div class="person-name">Daniel <span class="surname">Whitmore</span></div>
      <div class="person-role">Managing Director</div>
    </div>

    <div class="contact">
      <div class="offices">
        <p class="address">318 Harbor Lane<br>Eastport, NB 4127</p>
        <p class="address">210 Crescent Ave<br>Westbridge, NB 5390</p>
      </div>
      <p class="contact-line">
        <svg viewBox="0 0 12 12" aria-hidden="true"><path d="M2.5 1 L4.5 1 L5.2 3.6 L3.9 4.6 C4.6 6 5.9 7.3 7.4 8.1 L8.4 6.8 L11 7.5 L11 9.5 C11 10.3 10.3 11 9.5 11 C5 11 1 7 1 2.5 C1 1.7 1.7 1 2.5 1 Z" fill="var(--sky)"/></svg>
        (555) 210-4830
      </p>
      <p class="contact-line">
        <svg viewBox="0 0 12 12" aria-hidden="true"><rect x="1" y="2.5" width="10" height="7" rx="1" fill="var(--sky)"/><path d="M1.5 3 L6 6.5 L10.5 3" stroke="var(--paper)" stroke-width="1" fill="none"/></svg>
        info@valmontlaw.com
      </p>
      <p class="contact-line">
        <svg viewBox="0 0 12 12" aria-hidden="true"><circle cx="6" cy="6" r="5" fill="var(--sky)"/><path d="M1 6 H11 M6 1 C3.8 3.5 3.8 8.5 6 11 M6 1 C8.2 3.5 8.2 8.5 6 11" stroke="var(--paper)" stroke-width=".8" fill="none"/></svg>
        www.valmontlaw.com
      </p>
    </div>
  </section>

</main>
</body>
</html>
```